Singapore Peer-to-Peer Business Loans Site Needs a Name Card Design

We need a name card design for a new company based in Singapore called 'Ledgerbridge Capital (Singapore) Pte. Ltd.' or in short, 'LedcapSG'.
We run an online platform where small and medium enterprises can access seed capital from wealthy persons seeking high yield returns.
We need a name card design - We would like to see designs that use the colours red, black and/or grey, using any combination of the logos that we have attached. The final design should communicate transparency, innovativeness, financial savvy, and professionalism.
Target Market(s)
Sophisticated/expert financial investors and small & medium business owners.
Industry/Entity Type
Financial
Look and feel
Each slider illustrates characteristics of the customer's brand and the style your logo design should communicate.

```html
<!DOCTYPE html>
<html lang="en">
<head>
<meta charset="utf-8">
<title>LedcapSG Name Card</title>
<link rel="stylesheet" href="https://fonts.googleapis.com/css2?family=Questrial&display=swap">
<style>
  :root {
    --charcoal: #343940;
    --mist: #d1d2d4;
    --paper: #ffffff;
    --signal-red: #e4262b;
    --ink: #343940;
  }
  html, body {
    margin: 0;
    padding: 0;
    overflow: hidden;
    background: var(--paper);
  }
  .card {
    position: relative;
    width: 1200px;
    height: 702px;
    overflow: hidden;
    background: var(--charcoal);
    font-family: "Questrial", "Century Gothic", sans-serif;
  }
  .card-backdrop {
    position: absolute;
    inset: 0;
  }
  .brand {
    position: absolute;
    left: 415px;
    top: 118px;
    display: flex;
    align-items: center;
    gap: 22px;
  }
  .brand-square {
    width: 62px;
    height: 62px;
    background: var(--signal-red);
  }
  .brand-name {
    font-size: 118px;
    line-height: 1;
    color: var(--ink);
    letter-spacing: -2px;
  }
  .holder {
    position: absolute;
    left: 110px;
    top: 326px;
  }
  .holder-name {
    margin: 0;
    font-size: 42px;
    font-weight: 400;
    line-height: 1;
    color: var(--signal-red);
    letter-spacing: 0.5px;
  }
  .holder-role {
    margin: 8px 0 0;
    font-size: 30px;
    line-height: 1.1;
    color: var(--paper);
  }
  .contact {
    position: absolute;
    left: 0;
    right: 0;
    top: 532px;
    text-align: center;
    color: var(--paper);
  }
  .contact-line {
    margin: 0;
    font-size: 30px;
    line-height: 1.2;
  }
  .contact-line .accent { color: var(--signal-red); }
  .contact-line .divider {
    color: var(--signal-red);
    margin: 0 12px;
  }
  .contact-address {
    margin: 12px 0 0;
    font-size: 27px;
    line-height: 1.2;
  }
</style>
</head>
<body>
  <main class="card">
    <svg class="card-backdrop" width="1200" height="702" viewBox="0 0 1200 702" aria-hidden="true">
      <rect x="0" y="0" width="1200" height="16" fill="var(--paper)"/>
      <path d="M 18 0 C 300 272, 700 402, 1200 420 L 1200 0 Z" fill="var(--paper)"/>
      <path d="M 36 0 C 320 255, 720 390, 1200 407 L 1200 0 Z" fill="var(--mist)"/>
    </svg>

    <div class="brand">
      <span class="brand-square"></span>
      <span class="brand-name">LedcapSG</span>
    </div>

    <div class="holder">
      <h1 class="holder-name">MARCUS TAN</h1>
      <p class="holder-role">Financial Investor</p>
    </div>

    <div class="contact">
      <p class="contact-line">Direct <span class="accent">+</span> 65 6290 4417<span class="divider">|</span><span class="accent">hello</span>@ledcap.sg<span class="divider">|</span>www.<span class="accent">ledcap</span>.sg</p>
      <p class="contact-address">18 Harbour Quay, #14-02 Meridian Tower, Singapore 049317</p>
    </div>
  </main>
</body>
</html>
```